Simple Easy - Taekwondo brochure

I have the content and an idea of the layout I want. I need it to look nice and sharp.

It's a sided 8.5x11 colored brochure

please feel free to move things around and use the images provided

my website is www.brightpathdojo.example if you need an understanding of what the business is about.

all text content is on the website. please be creative!

Target Market(s)

Mothers...must by family friendly because it's for mothers to bring their kids.

Industry/Entity Type

Martial Art

Font styles to use
Other font styles liked:
• Lato

```html
<!DOCTYPE html>
<html lang="en">
<head>
<meta charset="utf-8">
<title>Bright Path Taekwondo – Brochure Inside Spread</title>
<link rel="stylesheet" href="https://fonts.googleapis.com/css2?family=Lato:wght@400;700&family=Roboto+Condensed:wght@400;500;700&display=swap">
<style>
  :root{
    --blue:#0a7bc1;
    --blue-dark:#0867a3;
    --charcoal:#353535;
    --charcoal-deep:#2b2b2b;
    --red:#d4121c;
    --white:#ffffff;
    --text-light:#ececec;
    --head-font:"Roboto Condensed", "Arial Narrow", sans-serif;
    --body-font:"Lato", Arial, sans-serif;
  }
  *{box-sizing:border-box;margin:0;padding:0}
  html,body{width:1200px;height:771px;overflow:hidden;background:var(--charcoal)}
  .spread{position:relative;width:1200px;height:771px;overflow:hidden;font-family:var(--body-font);color:var(--text-light)}
  .backdrop{position:absolute;inset:0;width:1200px;height:771px}

  .intro{position:absolute;left:0;top:91px;width:418px;text-align:center;font-family:var(--head-font);font-weight:500}
  .intro-lead{font-size:18px;line-height:24px;color:var(--white)}
  .benefits{list-style:none;margin-top:29px;font-size:20px;line-height:25px;text-transform:uppercase}
  .benefits .benefit-white{color:var(--white)}
  .benefits .benefit-red{color:var(--red)}

  .illustration{position:absolute}
  .illo-tiger-master{left:40px;top:370px;width:325px;height:390px;border-radius:40% 40% 20% 20%;
    background:radial-gradient(ellipse at 50% 45%, #d98a3a 0%, #f2f2f2 55%, rgba(255,255,255,0) 72%)}
  .illo-tiger-cub{left:540px;top:4px;width:190px;height:258px;border-radius:45%;
    background:radial-gradient(ellipse at 50% 45%, #e0913f 0%, #f5e9dc 55%, rgba(255,255,255,0) 72%)}
  .illo-bamboo{left:848px;top:584px;width:320px;height:122px;border-radius:30px;
    background:linear-gradient(90deg, rgba(122,156,60,.55), rgba(92,128,44,.45) 50%, rgba(70,104,40,.5))}

  .tenets{position:absolute;left:443px;top:250px;width:324px}
  .tenets-title{font-family:var(--head-font);font-weight:500;font-size:20px;color:var(--white)}
  .tenets-list{font-family:var(--head-font);font-weight:500;font-size:17px;line-height:22px;color:var(--white);margin-top:26px}
  .body-copy{font-size:13.6px;line-height:16.6px;text-align:justify;margin-top:20px}
  .section-label{font-family:var(--head-font);font-weight:500;font-size:17px;color:var(--white);margin-top:30px}

  .tenet{font-size:13.6px;line-height:16.8px;text-align:justify}
  .tenet p{margin:0}
  .tenet-tag{display:inline-block;background:var(--red);color:var(--white);font-family:var(--head-font);
    font-weight:500;font-size:18px;line-height:20px;padding:0 6px 0 5px;margin-right:3px}

  .tenet-courtesy{position:absolute;left:433px;top:538px;width:334px}
  .tenet-integrity{position:absolute;left:433px;top:700px;width:334px}
  .tenet-continued{position:absolute;left:857px;top:38px;width:288px}
  .tenet-perseverance{position:absolute;left:853px;top:92px;width:292px}
  .tenet-selfcontrol{position:absolute;left:853px;top:229px;width:292px}
  .tenet-spirit{position:absolute;left:853px;top:384px;width:292px}
</style>
</head>
<body>
<main class="spread">
  <svg class="backdrop" viewBox="0 0 1200 771" aria-hidden="true">
    <rect x="0" y="0" width="408" height="771" fill="var(--blue)"/>
    <polygon points="0,0 150,0 0,150" fill="var(--blue-dark)"/>
    <polygon points="0,530 231,363 408,545 408,771 0,771" fill="var(--white)"/>
    <polygon points="0,612 165,500 408,705 408,771 0,771" fill="var(--charcoal-deep)"/>
    <rect x="407" y="0" width="402" height="771" fill="var(--charcoal)"/>
    <polygon points="407,0 809,0 809,143 407,205" fill="var(--white)"/>
    <polygon points="407,0 540,0 407,200" fill="var(--blue)"/>
    <polygon points="616,0 809,0 809,100" fill="var(--charcoal)"/>
    <polygon points="690,210 809,148 809,242" fill="var(--red)"/>
    <polygon points="386,198 407,178 407,218" fill="var(--white)"/>
    <rect x="808" y="0" width="392" height="771" fill="var(--charcoal)"/>
    <rect x="808" y="536" width="392" height="235" fill="var(--red)"/>
    <polygon points="808,544 828,564 808,584" fill="var(--white)"/>
  </svg>

  <section class="intro">
    <p class="intro-lead">BRIGHT PATH TAEKWONDO is the prefect tool<br>to unlock your child’s potential</p>
    <ul class="benefits">
      <li class="benefit-white">Discipline</li>
      <li class="benefit-red">Self Defense</li>
      <li class="benefit-white">Focus</li>
      <li class="benefit-red">Self Respect</li>
      <li class="benefit-white">Leadership</li>
      <li class="benefit-red">Anti Bullying</li>
    </ul>
  </section>

  <div class="illustration illo-tiger-master" role="img" aria-label="Cartoon tiger in a white uniform and black belt holding a bamboo staff"></div>
  <div class="illustration illo-tiger-cub" role="img" aria-label="Cartoon tiger cub holding a magnifying glass"></div>
  <div class="illustration illo-bamboo" role="img" aria-label="Three cartoon bamboo characters growing from sprout to tall stalk"></div>

  <section class="tenets">
    <h2 class="tenets-title">The Five Tenets of Taekwondo</h2>
    <p class="tenets-list">Courtesy—Integrity—Perseverance—<br>Self-Control—Indomitable Spirit</p>
    <p class="body-copy">There are five universally accepted tenets of taekwondo accepted by both the Global Taekwondo Alliance (GTA) and the United Taekwondo Council (UTC). Bright Path Taekwondo bases our dojang rules and etiquette on the “Five Tenets of Taekwondo.”</p>
    <h3 class="section-label">(The Building of Character)</h3>
  </section>

  <article class="tenet tenet-courtesy">
    <p><span class="tenet-tag">#1. Courtesy –</span> Students will show courtesy to all others in the dojang, as well as people they meet outside of their formal training.</p>
    <p>Younger students will address adults as “Sir” or “Ma’am.”</p>
    <p>Students will bow to the American and S. Korean flags upon entering and exiting the dojang.</p>
  </article>

  <article class="tenet tenet-integrity">
    <p><span class="tenet-tag">#2. Integrity –</span> Students are expected to be honest and be willing to exhibit strong moral</p>
  </article>

  <article class="tenet tenet-continued">
    <p>principles that will help them distinguish between right and wrong.</p>
  </article>

  <article class="tenet tenet-perseverance">
    <p><span class="tenet-tag">#3. Perseverance –</span> Students must remember that they will never grow stronger by engaging their doubts. Therefore, students should be willing to confront their fears, battle back against their struggles, and never look for short-cuts when achieving their goals.</p>
  </article>

  <article class="tenet tenet-selfcontrol">
    <p><span class="tenet-tag">#4. Self-Control –</span> Students are expected to keep their emotions (thoughts and actions) in-check at all times, both inside and outside the dojang.</p>
    <p>Punctuality is essential because all classes start promptly at the designated times.</p>
    <p>Students are expected to keep the dojang clean and tidy.</p>
  </article>

  <article class="tenet tenet-spirit">
    <p><span class="tenet-tag">#5. Indomitable Spirit –</span> Students will consistently exhibit a full 100% effort in all they do inside and outside the dojang.</p>
    <p>Students must show courage when standing up for their beliefs and convictions inside and outside the dojang.</p>
  </article>
</main>
</body>
</html>
```